Website redesign

We've inherited a Tilecraft Website that we'd like to change to a Pagemill website to match our other sites.

Site I want redesigned is: https://www.corvellawings.com/
which will change to www.corvellaskytours.com.au

Our other websites I want it to match:
https://marloweskytours.com.au/
https://penfaricays.au/
https://tindaleskytours.com.au/
https://brightvalewings.com.au/

I do not want the design to deviate too much from the others, the main difference will be colours that need to align with the logo I've uploaded.

Pages I want:
Home
About Us
Gallery
News/Blog
Overflies
Half Day Tours
Full Day Tours
Transfers
Contact

Other pages will link to the other website - like on the other websites currently

```html
<!DOCTYPE html>
<html lang="en">
<head>
<meta charset="utf-8">
<title>Corvella Sky Tours</title>
<link rel="stylesheet" href="https://fonts.googleapis.com/css2?family=Archivo:wdth,wght@125,700;125,800&family=Lato:ital,wght@0,400;0,700;1,400&display=swap">
<style>
:root{
  --orange:#e8531d;
  --blue:#4a9fd8;
  --ink:#111111;
  --text:#333333;
  --muted:#666666;
  --line:#d6d6d6;
  --footer:#0e0e0e;
  --white:#ffffff;
}
*{box-sizing:border-box;margin:0;padding:0}
html,body{width:1200px;height:3896px;overflow:hidden}
body{position:relative;background:var(--white);font-family:"Lato",Arial,sans-serif;color:var(--text)}
.abs{position:absolute}
.heading{font-family:"Archivo",Arial,sans-serif;font-stretch:125%;font-weight:800;color:var(--ink);text-transform:uppercase;letter-spacing:1px}
.btn{display:inline-block;background:var(--orange);color:var(--white);font-size:15px;border-radius:6px;text-align:center}
.site-header{left:0;top:0;width:1200px;height:90px;background:var(--white)}
.brand{left:88px;top:28px;display:flex;align-items:center;gap:10px;font-weight:700;font-size:22px;color:var(--blue)}
.brand-dot{width:30px;height:30px;border-radius:50%;background:var(--blue)}
.nav{left:352px;top:36px;display:flex;gap:22px;font-size:13px;color:#444;align-items:center}
.nav-contact{left:992px;top:26px;width:120px;height:38px;line-height:38px}
.hero{left:0;top:90px;width:1200px;height:673px;background:linear-gradient(110deg,#4a5058 0%,#8a7560 45%,#b07a4c 70%,#6a4a36 100%)}
.hero-title{left:88px;top:300px;font-size:48px;line-height:54px;color:var(--white)}
.hero-btn{left:88px;top:479px;width:134px;height:38px;line-height:38px}
.scroll{left:578px;top:669px;width:44px;height:70px;border:2px solid var(--white);border-radius:22px;color:var(--white);text-align:center;line-height:66px;font-size:24px}
.section-title{left:0;width:1200px;text-align:center;font-size:32px}
.card{top:917px;width:244px;height:290px;border-radius:16px;overflow:hidden}
.card-label{position:absolute;left:12px;right:12px;bottom:8px;height:44px;background:var(--white);border-radius:8px;display:flex;align-items:center;justify-content:space-between;padding:0 16px;font-size:17px;color:var(--ink)}
.about-img{left:157px;top:1306px;width:435px;height:388px;border-radius:16px;background:linear-gradient(135deg,#2b2a24 0%,#3f4a44 40%,#1e6b7a 70%,#7fb4b8 100%)}
.clients{left:118px;top:1346px;width:210px;height:50px;background:var(--white);border-radius:10px;box-shadow:0 4px 14px rgba(0,0,0,.12)}
.avatar{position:absolute;top:7px;width:36px;height:36px;border-radius:50%;border:2px solid var(--white);background:#b88a6a}
.about-title{left:641px;top:1330px;font-size:32px;line-height:40px}
.about-copy{left:641px;top:1460px;width:450px;font-size:12px;line-height:22px;color:var(--muted)}
.feature{top:1547px;display:flex;align-items:center;gap:12px;font-size:17px;line-height:22px;color:var(--ink)}
.about-btn{left:641px;top:1627px;width:140px;height:36px;line-height:36px;font-size:14px}
.stat{top:1782px;width:258px;text-align:center}
.stat-icon{width:85px;height:72px;margin:0 auto;background:var(--blue);border-radius:4px;display:flex;align-items:center;justify-content:center}
.stat-num{font-family:"Archivo",Arial,sans-serif;font-stretch:125%;font-weight:700;font-size:30px;color:var(--ink);margin-top:8px}
.stat-label{font-size:14px;color:#444;margin-top:4px}
.divider-v{top:1782px;width:1px;height:142px;background:var(--line)}
.blogs{left:0;top:2012px;width:1200px;height:500px;background:linear-gradient(180deg,#f1f1f1 0%,#e3e3e3 60%,#c9c4bd 100%)}
.blog{top:2136px;width:288px}
.blog-img{width:288px;height:218px;border-radius:16px}
.blog-body{margin-top:16px;border-left:2px solid var(--blue);padding-left:14px}
.blog-date{font-size:11px;color:var(--orange)}
.blog-title{font-size:15px;line-height:21px;color:var(--ink);margin-top:6px}
.blog-link{font-size:13px;color:var(--orange);text-decoration:underline;margin-top:10px}
.quote{left:262px;top:2646px;width:676px;text-align:center;font-style:italic;font-size:15.5px;line-height:25px;color:var(--muted)}
.stars{left:0;top:2748px;width:1200px;text-align:center;color:#f0a020;font-size:22px;letter-spacing:4px}
.client{left:0;top:2782px;width:1200px;text-align:center;font-size:14px;color:var(--ink)}
.dots{left:582px;top:2817px;display:flex;gap:5px}
.dot{width:8px;height:8px;border-radius:50%;background:#bbb}
.gal{top:2967px;width:246px;height:218px;border-radius:16px}
.gal-link{left:437px;top:3044px;width:68px;height:68px;border-radius:50%;background:var(--blue);display:flex;align-items:center;justify-content:center}
.footer{left:0;top:3415px;width:1200px;height:481px;background:var(--footer)}
.cta{left:89px;top:3329px;width:1022px;height:162px;border-radius:22px;background:var(--blue);overflow:hidden}
.cta-photo{position:absolute;left:650px;top:0;width:372px;height:162px;background:linear-gradient(120deg,#6d8a4a 0%,#a3b86a 50%,#c9a46a 100%);clip-path:polygon(10% 0,100% 0,100% 100%,22% 100%)}
.cta-title{left:125px;top:3355px;font-size:28px;line-height:36px;color:var(--white)}
.cta-btn{top:3431px;height:38px;line-height:36px;width:114px;border-radius:6px;font-size:14px;text-align:center}
.foot-brand{left:92px;top:3632px;display:flex;align-items:center;gap:12px;font-size:26px;font-weight:700;color:var(--blue)}
.foot-head{font-family:"Archivo",Arial,sans-serif;font-stretch:125%;font-weight:700;font-size:18px;color:var(--white);text-transform:uppercase;letter-spacing:1px}
.foot-col{top:3554px;color:var(--white);font-size:12px}
.foot-links{margin-top:10px;line-height:22px}
.contact-item{display:flex;gap:8px;margin-top:10px;line-height:18px}
.socials{display:flex;gap:8px;margin-top:14px}
.social{width:36px;height:36px;border-radius:50%;background:#2a2a2a;border:1px solid #444}
.social.on{background:var(--blue);border-color:var(--blue)}
.foot-rule{left:88px;top:3839px;width:1024px;height:1px;background:#333}
.copyright{left:0;top:3862px;width:1200px;text-align:center;font-size:14px;color:var(--white)}
.to-top{left:1133px;top:3820px;width:40px;height:40px;border-radius:50%;background:var(--blue);display:flex;align-items:center;justify-content:center}
</style>
</head>
<body>

<header class="abs site-header">
  <div class="abs brand"><span class="brand-dot"></span>Corvella Sky Tours</div>
  <nav class="abs nav">
    <svg width="18" height="16" viewBox="0 0 18 16"><path d="M9 1 1 8h2v7h4v-4h4v4h4V8h2z" fill="#4a9fd8"/></svg>
    <span>About Us</span><span>Gallery</span><span>News/Blog</span><span>Overflies</span><span>Half Day Tours</span><span>Full Day Tours</span><span>Transfers</span>
  </nav>
  <span class="abs btn nav-contact">Contact Us</span>
</header>

<section class="abs hero" role="img" aria-label="Traveller with backpack watching an aircraft on the runway at sunset"></section>
<h1 class="abs heading hero-title">Scenic Flights<br>Day Tours Charter<br>Airwork</h1>
<span class="abs btn hero-btn">Book Now</span>
<div class="abs scroll">↓</div>

<h2 class="abs heading section-title" style="top:850px">Explore Our Excursions</h2>
<div class="abs card" style="left:88px;background:linear-gradient(160deg,#b08060,#6a5040)" role="img" aria-label="Passenger looking through binoculars from an aircraft">
  <div class="card-label">Overflies<svg width="16" height="16" viewBox="0 0 16 16"><path d="M3 13 13 3M5 3h8v8" stroke="#111" stroke-width="1.6" fill="none"/></svg></div></div>
<div class="abs card" style="left:347px;background:linear-gradient(180deg,#2f7fc0,#4f8a5a)" role="img" aria-label="Hiker with arms outstretched above a mountain valley">
  <div class="card-label">Half Day tours<svg width="16" height="16" viewBox="0 0 16 16"><path d="M3 13 13 3M5 3h8v8" stroke="#111" stroke-width="1.6" fill="none"/></svg></div></div>
<div class="abs card" style="left:607px;background:linear-gradient(160deg,#6fa04a,#b04030)" role="img" aria-label="Group of friends celebrating on a vehicle in the forest">
  <div class="card-label">Full Day tours<svg width="16" height="16" viewBox="0 0 16 16"><path d="M3 13 13 3M5 3h8v8" stroke="#111" stroke-width="1.6" fill="none"/></svg></div></div>
<div class="abs card" style="left:867px;background:linear-gradient(160deg,#e8e8e8,#b0a89e)" role="img" aria-label="Travel consultants planning a custom trip">
  <div class="card-label">Custom Tours<svg width="16" height="16" viewBox="0 0 16 16"><path d="M3 13 13 3M5 3h8v8" stroke="#111" stroke-width="1.6" fill="none"/></svg></div></div>

<div class="abs about-img" role="img" aria-label="Aerial view of rugged coastline and turquoise surf"></div>
<div class="abs clients">
  <span class="avatar" style="left:2px" role="img" aria-label="Client portrait"></span>
  <span class="avatar" style="left:22px;background:#c9a080" role="img" aria-label="Client portrait"></span>
  <span class="avatar" style="left:42px;background:#8a6a50" role="img" aria-label="Client portrait"></span>
  <span style="position:absolute;left:102px;top:6px;font-weight:700;font-size:17px;color:var(--orange)">156+</span>
  <span style="position:absolute;left:102px;top:28px;font-size:11px;color:#444">Satisfied Clients</span>
</div>
<h2 class="abs heading about-title">Your Gateway To<br>Geraldton's Aerial<br>Wonders</h2>
<p class="abs about-copy">At Corvella Sky Tours, we are passionate about sharing the breathtaking beauty of Geraldton and its surrounding areas from a unique vantage point.</p>
<div class="abs feature" style="left:641px"><span style="font-weight:800;color:var(--blue);font-size:20px">35</span><span>35 Years<br>Experience</span></div>
<div class="abs feature" style="left:872px"><svg width="36" height="36" viewBox="0 0 36 36"><circle cx="18" cy="18" r="14" fill="none" stroke="#4a9fd8" stroke-width="2"/><path d="M6 24 28 10l-6 14-4-5z" fill="#4a9fd8"/></svg><span>Wide range<br>of Tours</span></div>
<span class="abs btn about-btn">Discover More</span>

<div class="abs stat" style="left:83px"><div class="stat-icon"><svg width="44" height="44" viewBox="0 0 44 44"><circle cx="22" cy="22" r="16" fill="none" stroke="#fff" stroke-width="2"/><path d="M8 30 36 12" stroke="#fff" stroke-width="2"/></svg></div><div class="stat-num">15+</div><div class="stat-label">Scenic Flights &amp; Charters</div></div>
<div class="abs divider-v" style="left:341px"></div>
<div class="abs stat" style="left:341px"><div class="stat-icon"><svg width="44" height="44" viewBox="0 0 44 44"><path d="M28 6a7 7 0 0 1 7 7c0 6-7 12-7 12s-7-6-7-12a7 7 0 0 1 7-7z" fill="none" stroke="#fff" stroke-width="2"/><circle cx="12" cy="30" r="5" fill="none" stroke="#fff" stroke-width="2"/><path d="M12 36h20" stroke="#fff" stroke-width="2" stroke-dasharray="3 3"/></svg></div><div class="stat-num">5+</div><div class="stat-label">Destinations</div></div>
<div class="abs divider-v" style="left:600px"></div>
<div class="abs stat" style="left:600px"><div class="stat-icon"><svg width="44" height="44" viewBox="0 0 44 44"><rect x="8" y="20" width="28" height="10" rx="3" fill="none" stroke="#fff" stroke-width="2"/><circle cx="14" cy="32" r="3" fill="#fff"/><circle cx="30" cy="32" r="3" fill="#fff"/><path d="M12 20l4-8h12l4 8" fill="none" stroke="#fff" stroke-width="2"/></svg></div><div class="stat-num">550+</div><div class="stat-label">Scenic Trips</div></div>
<div class="abs divider-v" style="left:858px"></div>
<div class="abs stat" style="left:858px"><div class="stat-icon"><svg width="44" height="44" viewBox="0 0 44 44"><rect x="10" y="6" width="24" height="22" rx="2" fill="none" stroke="#fff" stroke-width="2"/><circle cx="22" cy="17" r="6" fill="none" stroke="#fff" stroke-width="2"/><path d="M6 36h26l6-6" fill="none" stroke="#fff" stroke-width="2"/></svg></div><div class="stat-num">3,600+</div><div class="stat-label">Happy Customers</div></div>

<section class="abs blogs" role="img" aria-label="Faded coastal landscape backdrop"></section>
<h2 class="abs heading section-title" style="top:2074px">Our Blogs</h2>
<article class="abs blog" style="left:148px"><div class="blog-img" style="background:linear-gradient(180deg,#4a7ab0,#c8cfc8 55%,#e8e8e0)" role="img" aria-label="Coastal lookout sign among dune shrubs"></div><div class="blog-body"><div class="blog-date">23 MAR, 2024</div><div class="blog-title">Lorem Ipsum Is Simply Dummy<br>Text Of The Printing</div><div class="blog-link">Read More</div></div></article>
<article class="abs blog" style="left:456px"><div class="blog-img" style="background:linear-gradient(150deg,#1a5a8a,#3aa6b8 50%,#7fd0c8)" role="img" aria-label="Reef islands seen from an aircraft window"></div><div class="blog-body"><div class="blog-date">23 MAR, 2024</div><div class="blog-title">Lorem Ipsum Is Simply Dummy<br>Text Of The Printing</div><div class="blog-link">Read More</div></div></article>
<article class="abs blog" style="left:764px"><div class="blog-img" style="background:linear-gradient(180deg,#6f8a9a,#8a7a5a 45%,#2a6a9a)" role="img" aria-label="Aerial view of a coastal town and bay"></div><div class="blog-body"><div class="blog-date">23 MAR, 2024</div><div class="blog-title">Lorem Ipsum Is Simply Dummy<br>Text Of The Printing</div><div class="blog-link">Read More</div></div></article>

<h2 class="abs heading section-title" style="top:2590px">What Our Client Says</h2>
<p class="abs quote">It is a long established fact that a reader will be distracted by the readable content of a page when looking at its layout. The point of using Lorem Ipsum is that it has a more-or-less normal distribution of letters, as opposed to using 'Content here, content here', making it look like readable English.</p>
<div class="abs stars">★★★★★</div>
<div class="abs client">Alex Morgan</div>
<div class="abs dots"><span class="dot"></span><span class="dot" style="background:#111"></span><span class="dot"></span></div>

<h2 class="abs heading section-title" style="top:2905px">Our Gallery</h2>
<div class="abs gal" style="left:89px;background:linear-gradient(150deg,#a0703a,#6a5a40)" role="img" aria-label="Aerial view of a river gorge"></div>
<div class="abs gal" style="left:348px;background:linear-gradient(180deg,#7a6a5a,#3a4a3a)" role="img" aria-label="Forest and river under stormy sky"></div>
<div class="abs gal" style="left:606px;background:linear-gradient(160deg,#4a90c8,#d890a8 45%,#6a7a5a)" role="img" aria-label="Pink lake beside the coast from the air"></div>
<div class="abs gal" style="left:865px;background:linear-gradient(160deg,#1a8ab0,#6ad0c8)" role="img" aria-label="Island jetty surrounded by turquoise water"></div>
<div class="abs gal-link"><svg width="28" height="28" viewBox="0 0 28 28"><path d="M12 16l4-4M10 13l-3 3a3.5 3.5 0 0 0 5 5l3-3M18 15l3-3a3.5 3.5 0 0 0-5-5l-3 3" stroke="#fff" stroke-width="2.2" fill="none" stroke-linecap="round"/></svg></div>

<footer class="abs footer"></footer>
<div class="abs cta"><div class="cta-photo" role="img" aria-label="Traveller in a hat taking photos outdoors"></div></div>
<h2 class="abs heading cta-title">Fly With Us And Discover<br>Western Australia's Beauty!</h2>
<span class="abs btn cta-btn" style="left:125px">Contact Us</span>
<span class="abs cta-btn" style="left:248px;border:1.5px solid #fff;color:#fff">Book Now</span>

<div class="abs foot-brand"><span class="brand-dot" style="width:38px;height:38px"></span>Corvella Sky Tours</div>
<div class="abs foot-col" style="left:449px"><div class="foot-head">Quick Links</div><div class="foot-links">Home<br>About Us<br>Gallery<br>News/Blog<br>Overflies<br>Half Day Tours<br>Full Day Tours<br>Transfers</div></div>
<div class="abs foot-col" style="left:697px"><div class="foot-head">Contact Us</div>
  <div class="contact-item"><svg width="12" height="12" viewBox="0 0 12 12"><path d="M2 1h3l1 3-2 1a7 7 0 0 0 3 3l1-2 3 1v3c-6 0-9-3-9-9z" fill="#4a9fd8"/></svg><span>Phone*<br>08 9000 4127</span></div>
  <div class="contact-item" style="margin-top:18px"><svg width="12" height="12" viewBox="0 0 12 12"><rect x="1" y="2" width="10" height="8" fill="#4a9fd8"/><path d="M1 2l5 4 5-4" stroke="#0e0e0e" fill="none"/></svg><span>Email*<br>info@corvellaskytours.com.au</span></div>
  <div class="contact-item" style="margin-top:18px"><svg width="12" height="12" viewBox="0 0 12 12"><path d="M6 1a4 4 0 0 1 4 4c0 3-4 7-4 7S2 8 2 5a4 4 0 0 1 4-4z" fill="#4a9fd8"/></svg><span>Loction*<br>Some address line<br>goes here city name</span></div>
</div>
<div class="abs foot-col" style="left:941px"><div class="foot-head">Follow Us</div>
  <div class="socials"><span class="social on"></span><span class="social"></span><span class="social"></span><span class="social"></span></div></div>
<div class="abs foot-rule"></div>
<div class="abs copyright">© Copyright 2025 Corvella Sky Tours | All rights reserved</div>
<div class="abs to-top"><svg width="14" height="14" viewBox="0 0 14 14"><path d="M3 9l4-4 4 4" stroke="#fff" stroke-width="2" fill="none"/></svg></div>

</body>
</html>
```